Business card design needed

I run a life coaching business.
I coach individuals, businesses & groups.
Our aim is create massive change for our clients.
I would like to see a card that is inspirational, something that provokes the thought of achieving your personal best.
Be your own inspiration is a phrase I am considering using.

Target Market(s)

People who are looking to create a massive change in their lives.

Industry/Entity Type

Life Coaching

Contact Information for Business Card

Harbor Light Coaching
Neil Pardoe
Head Coach
email neil@vorunel.com.au
Mob 0412 586 337

Logo styles of interest
Abstract Logo
Requirements
Must have
• I wouldlike to have a free introductory offer on the reverse side of the card.
It would read something like:
Is coaching for me/you?
Try a free 45 minute session.
Book now call or email for your appointment.

```html
<!DOCTYPE html>
<html lang="en">
<head>
<meta charset="utf-8">
<title>Harbor Light Coaching – Business Card</title>
<link rel="stylesheet" href="https://fonts.googleapis.com/css2?family=Cormorant+Garamond:ital,wght@1,500;1,600&display=swap">
<style>
  :root {
    --crimson: #7c0a2c;
    --crimson-deep: #4a0618;
    --black: #000000;
    --gold: #c8962c;
    --card-w: 1200px;
    --card-h: 686px;
  }
  html, body {
    margin: 0;
    padding: 0;
    width: var(--card-w);
    height: var(--card-h);
    overflow: hidden;
    background: var(--black);
  }
  .card {
    position: relative;
    width: var(--card-w);
    height: var(--card-h);
    overflow: hidden;
    font-family: "Cormorant Garamond", "Garamond", serif;
    font-style: italic;
    font-variant-numeric: lining-nums;
    color: var(--gold);
  }
  .card-backdrop {
    position: absolute;
    inset: 0;
    width: 100%;
    height: 100%;
  }
  .card-text {
    position: absolute;
    margin: 0;
    line-height: 1;
    white-space: nowrap;
  }
  .holder-name {
    left: 67px;
    top: 62px;
    font-size: 60px;
    font-weight: 600;
  }
  .holder-role {
    left: 68px;
    top: 131px;
    font-size: 37px;
    font-weight: 500;
  }
  .business-name {
    left: 0;
    width: 100%;
    top: 270px;
    text-align: center;
    padding-left: 12px;
    box-sizing: border-box;
    font-size: 79px;
    font-weight: 600;
    letter-spacing: 0.5px;
  }
  .contact-email {
    left: 70px;
    top: 488px;
    font-size: 36px;
    font-weight: 500;
  }
  .contact-phone {
    left: 70px;
    top: 551px;
    font-size: 36px;
    font-weight: 500;
  }
</style>
</head>
<body>
  <div class="card">
    <svg class="card-backdrop" viewBox="0 0 1050 600" preserveAspectRatio="none" aria-hidden="true">
      <defs>
        <linearGradient id="upper-fade" x1="0" y1="0" x2="1" y2="0">
          <stop offset="0" stop-color="var(--crimson)"/>
          <stop offset="0.5" stop-color="var(--crimson-deep)"/>
          <stop offset="1" stop-color="var(--black)"/>
        </linearGradient>
        <linearGradient id="lower-fade" x1="0" y1="0" x2="1030" y2="0" gradientUnits="userSpaceOnUse">
          <stop offset="0" stop-color="var(--black)"/>
          <stop offset="0.45" stop-color="var(--crimson-deep)"/>
          <stop offset="1" stop-color="var(--crimson)"/>
        </linearGradient>
      </defs>
      <rect class="upper-band" x="0" y="0" width="1050" height="600" fill="url(#upper-fade)"/>
      <path class="lower-sweep" d="M0,180 C300,172 560,220 760,295 C950,370 1030,480 1030,600 L0,600 Z" fill="url(#lower-fade)"/>
    </svg>

    <h1 class="card-text holder-name">Neil Pardoe</h1>
    <p class="card-text holder-role">Head Coach</p>
    <h2 class="card-text business-name">Harbor Light Coaching</h2>
    <p class="card-text contact-email">neil@vorunel.com.au</p>
    <p class="card-text contact-phone">Phone: 0412 586 337</p>
  </div>
</body>
</html>
```